Awesome product template needed now!

I need a product template for online presentation of products. I have attached a screenshot of something similar to what the design specs are.

Target Market(s)

Purchasers of antiquities, collectable currency and fine art

Requirements
Must have
• See attachment.
White background for product placement is a must have
Nice to have
• See attachment

```html
<!DOCTYPE html>
<html lang="en">
<head>
<meta charset="utf-8">
<title>Product Presentation Template</title>
<link rel="stylesheet" href="https://fonts.googleapis.com/css2?family=Open+Sans:wght@700&display=swap">
<style>
  :root {
    --wood-dark: #2e1c12;
    --wood-mid: #4d3020;
    --wood-light: #6a4428;
    --gold-light: #fbd862;
    --gold-mid: #f7b648;
    --gold-deep: #f3a03a;
    --mat-black: #000000;
    --placement-white: #ffffff;
    --placeholder-line: #a89a8a;
    --holo-green: #b8d9a4;
    --holo-cream: #f4f0b8;
    --holo-lilac: #b6aec6;
    --holo-cyan: #86d0d0;
  }
  html, body {
    margin: 0;
    padding: 0;
    width: 1200px;
    height: 600px;
    overflow: hidden;
    font-family: "Open Sans", sans-serif;
  }
  .canvas {
    position: relative;
    width: 1200px;
    height: 600px;
    overflow: hidden;
  }
  .wood-backdrop {
    position: absolute;
    inset: 0;
    background:
      repeating-linear-gradient(90deg, rgba(0,0,0,0.35) 0 2px, transparent 2px 88px),
      linear-gradient(180deg, var(--wood-light) 0%, var(--wood-mid) 40%, var(--wood-dark) 100%);
  }
  .gold-frame {
    position: absolute;
    left: 48px;
    top: 48px;
    width: 1103px;
    height: 503px;
    background: linear-gradient(90deg,
      var(--gold-mid) 0%, var(--gold-light) 6%, var(--gold-deep) 30%,
      var(--gold-deep) 60%, var(--gold-light) 88%, var(--gold-mid) 100%);
    box-shadow: 0 6px 14px rgba(0,0,0,0.55);
  }
  .gold-frame::before {
    content: "";
    position: absolute;
    inset: 0;
    border: 4px solid rgba(255,255,255,0.12);
    border-bottom-color: rgba(0,0,0,0.08);
    border-right-color: rgba(0,0,0,0.06);
  }
  .display-mat {
    position: absolute;
    left: 21px;
    top: 21px;
    width: 1062px;
    height: 462px;
    background: var(--mat-black);
  }
  .authenticity-label {
    position: absolute;
    left: 95px;
    top: 44px;
    width: 129px;
    height: 375px;
    border-radius: 19px;
    background: linear-gradient(118deg,
      var(--holo-green) 0%, var(--holo-cream) 22%, var(--holo-lilac) 42%,
      var(--holo-cyan) 62%, var(--holo-cream) 82%, var(--holo-green) 100%);
  }
  .product-placement {
    position: absolute;
    left: 292px;
    top: 43px;
    width: 676px;
    height: 319px;
    background: var(--placement-white);
    border: 2px dotted var(--placeholder-line);
    box-sizing: border-box;
  }
</style>
</head>
<body>
  <main class="canvas">
    <div class="wood-backdrop" role="img" aria-label="Dark wooden plank wall texture"></div>
    <section class="gold-frame">
      <div class="display-mat">
        <div class="authenticity-label" role="img" aria-label="Holographic authenticity seal with repeated diagonal wording and fox head emblem"></div>
        <div class="product-placement" aria-label="Product placement area"></div>
      </div>
    </section>
  </main>
</body>
</html>
```